Legal Agribusiness Capability Brochure Design

Design A4 sized 6 page Legal Agribusiness Capability Brochure. Design is to be consistent with current marketing materials - logo, letterhead, website and business card to be provided.
Cover page - Firm name and logo, Agribusiness Capability Statement heading with image 1 below
Inside cover page - About Us section with image 2 below then Awards section below image
Inside middle page - Our Expertise with image 3 below
Inside back page - Our Experience with image 4 below
Back page - Senior Lawyers with image 5 below
Outside Middle Back Page - Contact Us with image 6
Updates

To provide more details to designers for brochure

Target Market(s)

Agribusiness - Australia

Industry/Entity Type

Legal

Colors

Designer to choose colors to be used in the design.

Requirements
Must have
• Use content from uloaded file - Agribusiness Brochure Content
• Use images uploaded
• Professional appearance
• Consistent with current marketing and website https://ferngatelegal.com.au/

```html
<!DOCTYPE html>
<html lang="en">
<head>
<meta charset="utf-8">
<title>Ferngate Legal – Agribusiness Capability Statement</title>
<link href="https://fonts.googleapis.com/css2?family=Oswald:wght@500;600&family=Open+Sans:wght@400;600;700&display=swap" rel="stylesheet">
<style>
  :root{
    --blue:#1f80d2;
    --blue-light:#2aa5e6;
    --blue-dark:#1668b3;
    --ink:#3a3a3a;
    --page:#ffffff;
    --canvas:#eeeeee;
    --gold:#c9a94a;
  }
  *{box-sizing:border-box;margin:0;padding:0}
  html,body{width:1200px;height:1200px;overflow:hidden;background:var(--canvas)}
  body{position:relative;font-family:"Open Sans",Arial,sans-serif;color:var(--ink)}
  .panel{position:absolute;width:370px;height:540px;background:var(--page);overflow:hidden;box-shadow:0 6px 18px rgba(0,0,0,.18)}
  .row-top .panel{top:30px}
  .row-bottom .panel{top:620px}
  .col-1{left:45px}.col-2{left:415px}.col-3{left:785px}
  .strip{height:10px;background:linear-gradient(90deg,var(--blue),var(--blue-light))}
  .masthead{height:70px;display:flex;align-items:center;justify-content:space-between;padding:0 14px}
  .seal{width:44px;height:44px;border-radius:50%;border:3px double #333}
  .award{width:46px;height:46px;border-radius:50%;border:2px solid var(--gold)}
  .brand{display:flex;align-items:center;gap:6px}
  .brand-mark{width:24px;height:24px;background:var(--blue)}
  .brand-name{font-weight:700;font-size:17px;color:var(--blue);letter-spacing:.5px}
  .band{background:linear-gradient(90deg,var(--blue-light),var(--blue));color:#fff;font-family:"Oswald",Impact,sans-serif;font-weight:600;text-transform:uppercase;text-align:center;font-size:18px;padding:3px 0;letter-spacing:.3px}
  .body{padding:8px 20px;font-size:7.3px;line-height:1.35}
  .body p{margin-bottom:4px}
  ul.dots{list-style:none}
  ul.dots li{position:relative;padding-left:11px;margin-bottom:3px}
  ul.dots li::before{content:"";position:absolute;left:1px;top:3px;width:4px;height:4px;border-radius:50%;background:#222}
  .photo{position:absolute;left:0;right:0;bottom:0}
  .corners{position:absolute;inset:0;width:100%;height:100%}

  /* cover */
  .cover-title{margin-top:32px;padding:12px 0 14px;text-align:left;padding-left:62px}
  .cover-title .main{font-size:30px;line-height:1.05;display:block}
  .cover-title .sub{font-size:18px;display:block}
  .photo-sheep{top:300px;background:linear-gradient(180deg,#d8c8a8 0%,#c9ac7e 45%,#8a6a48 75%,#6d4b33 100%)}
  .photo-harvest{top:290px;background:linear-gradient(180deg,#c9c2b6 0%,#a89f90 30%,#c8a042 55%,#b48a3a 80%,#7f6128 100%)}

  /* contact */
  .contact-band{padding:4px 0 6px}
  .contact-band .intro{font-family:"Open Sans",Arial,sans-serif;font-weight:400;text-transform:none;font-size:7.5px;line-height:1.35;padding:6px 36px 0;letter-spacing:0}
  .offices{display:flex;gap:20px;padding:8px 28px 0}
  .office{flex:1;font-size:7.3px;line-height:1.4;color:var(--blue-dark)}
  .line{display:flex;gap:6px;align-items:flex-start;margin-bottom:4px}
  .line svg{flex:none;width:10px;height:10px;margin-top:1px}
  .web{display:flex;justify-content:flex-end;gap:6px;padding:6px 28px 0;font-size:7.8px;font-weight:700;color:var(--blue-dark)}
  .web svg{width:10px;height:10px}

  /* lawyers */
  .lawyer-head{display:flex;justify-content:space-between;align-items:flex-end;padding:6px 20px 0 30px;height:48px}
  .lawyer-name{font-weight:700;font-size:13px;color:var(--blue);padding-bottom:6px}
  .portrait{width:38px;height:44px;background:linear-gradient(180deg,#cfd6de,#2f3540)}
  .bio{background:linear-gradient(90deg,var(--blue),var(--blue-light));color:#fff;padding:6px 24px 6px 30px;font-size:7px;line-height:1.35}
  .ranks{padding:8px 24px 0 30px;font-size:7px}
  .ranks strong{font-size:7.5px}
  .ranks ul{margin-top:3px}
  .photo-vine{height:64px;background:linear-gradient(180deg,#9fc4e6 0%,#d9e6ef 35%,#7d7a35 60%,#7c3d2a 100%)}

  .photo-canola{height:60px;background:linear-gradient(180deg,#9ec3e4 0%,#cfe0ea 30%,#6f9a3e 55%,#e7d21f 80%,#f0dc2a 100%)}
  .photo-cattle{height:88px;background:linear-gradient(180deg,#d9c8a0 0%,#9a8463 45%,#4a3d2e 80%,#2d261e 100%)}
  .photo-sunset{height:62px;background:linear-gradient(180deg,#f7c66a 0%,#f19a2b 50%,#b8541a 80%,#5a2a12 100%)}
  .exp .body{font-size:7px;line-height:1.33;padding-top:7px}
  .exp ul.dots li{margin-bottom:5px}
</style>
</head>
<body>

<div class="row-top">
  <!-- Cover -->
  <section class="panel col-1 cover">
    <div class="strip"></div>
    <header class="masthead">
      <span class="seal" aria-hidden="true"></span>
      <div class="brand"><span class="brand-mark"></span><span class="brand-name">FERNGATE LEGAL</span></div>
      <span class="award" aria-hidden="true"></span>
    </header>
    <h1 class="band cover-title"><span class="main">Agribusiness</span><span class="sub">Capability Statement</span></h1>
    <div class="photo photo-sheep" role="img" aria-label="Flock of sheep standing on a dry paddock under a pale sky">
      <svg class="corners" viewBox="0 0 370 240" preserveAspectRatio="none" aria-hidden="true">
        <polygon points="220,0 370,0 370,150" fill="#1f80d2"/>
        <polygon points="0,120 0,240 130,240" fill="#1f80d2"/>
      </svg>
    </div>
  </section>

  <!-- Contact -->
  <section class="panel col-2 contact">
    <div class="strip"></div>
    <header class="masthead">
      <span class="seal" aria-hidden="true"></span>
      <div class="brand"><span class="brand-mark"></span><span class="brand-name">FERNGATE LEGAL</span></div>
      <span class="award" aria-hidden="true"></span>
    </header>
    <div class="band contact-band">
      <h2>Contact Us</h2>
      <p class="intro">If you have any questions or require any assistance in relation to agribusiness law, please contact us at our Geraldton or Perth office.</p>
    </div>
    <div class="offices">
      <div class="office">
        <div class="line"><svg viewBox="0 0 10 10"><path d="M5 1 1 5h1.5v4h2V6.5h1V9h2V5H9z" fill="#1f80d2"/></svg><span>Geraldton Office<br>Suite 4, Coral Bay House<br>12 Saltbush Lane<br>Geraldton WA 6530</span></div>
        <div class="line"><svg viewBox="0 0 10 10"><path d="M1 4c0-2 8-2 8 0v1H7V4H3v1H1zM2 6h6l1 3H1z" fill="#1f80d2"/></svg><span>+61 8 9000 1100 / +61 8 9000 1101</span></div>
        <div class="line"><svg viewBox="0 0 10 10"><circle cx="5" cy="5" r="4.5" fill="#1f80d2"/><rect x="2.5" y="3.5" width="5" height="3" fill="#fff"/></svg><span>info@ferngatelegal.com.au</span></div>
      </div>
      <div class="office">
        <div class="line"><svg viewBox="0 0 10 10"><path d="M5 1 1 5h1.5v4h2V6.5h1V9h2V5H9z" fill="#1f80d2"/></svg><span>Perth Office<br>88 Kestrel Avenue<br>West Perth WA 6005</span></div>
        <div class="line" style="margin-top:19px"><svg viewBox="0 0 10 10"><path d="M1 4c0-2 8-2 8 0v1H7V4H3v1H1zM2 6h6l1 3H1z" fill="#1f80d2"/></svg><span>+61 8 9000 2200 / +61 8 9000 2201</span></div>
        <div class="line"><svg viewBox="0 0 10 10"><circle cx="5" cy="5" r="4.5" fill="#1f80d2"/><rect x="2.5" y="3.5" width="5" height="3" fill="#fff"/></svg><span>info@ferngatelegal.com.au</span></div>
      </div>
    </div>
    <div class="web"><svg viewBox="0 0 10 10"><circle cx="5" cy="5" r="4.2" fill="none" stroke="#1f80d2" stroke-width="1.2"/><path d="M1 5h8M5 1v8" stroke="#1f80d2" stroke-width=".8"/></svg><span>www.ferngatelegal.com.au</span></div>
    <div class="photo photo-harvest" style="top:300px" role="img" aria-label="Yellow combine harvester cutting a golden wheat crop under a hazy sky">
      <svg class="corners" viewBox="0 0 370 240" preserveAspectRatio="none" aria-hidden="true">
        <polygon points="0,0 150,0 0,150" fill="#1f80d2"/>
        <polygon points="370,140 370,240 250,240" fill="#1f80d2"/>
      </svg>
    </div>
  </section>

  <!-- Senior lawyers -->
  <section class="panel col-3 lawyers">
    <div class="strip"></div>
    <header class="masthead">
      <span class="seal" aria-hidden="true"></span>
      <div class="brand"><span class="brand-mark"></span><span class="brand-name">FERNGATE LEGAL</span></div>
      <span class="award" aria-hidden="true"></span>
    </header>
    <h2 class="band">Senior Lawyers</h2>
    <div class="lawyer-head">
      <h3 class="lawyer-name">DANIEL BROOKE – PRINCIPAL</h3>
      <div class="portrait" role="img" aria-label="Portrait photo of Daniel Brooke"></div>
    </div>
    <div class="bio">
      <p>Daniel has practised exclusively as a commercial lawyer for over 20 years, initially at Perth law firms and since 2009 in Geraldton.</p>
      <p>In 2011, Daniel established Ferngate Legal in Geraldton and expanded with the opening of a Perth office in 2017.</p>
      <p>Daniel has advised on a large number of commercial matters and disputes, particularly in relation to agribusiness, business, property, wills and estates. He has a proven track record of delivering results to clients, especially in relation to more complex commercial transactions and disputes.</p>
      <p>Daniel has a specific interest in agribusiness, primarily due to his family being involved in agribusiness for several generations.</p>
    </div>
    <div class="ranks">
      <strong>Ranked by Harlow's Guide as a:</strong>
      <ul class="dots">
        <li>"Preeminent Agribusiness Lawyer – Western Australia, 2019" (Top 2 in W.A.)</li>
        <li>"Leading Agribusiness Lawyer – Western Australia, 2018" (Top 5 in W.A.)</li>
        <li>"Leading Agribusiness Lawyer – Western Australia, 2017" (Top 7 in W.A.)</li>
      </ul>
    </div>
    <div class="lawyer-head">
      <h3 class="lawyer-name">GRAHAM BROOKE – CONSULTANT</h3>
      <div class="portrait" role="img" aria-label="Portrait photo of Graham Brooke"></div>
    </div>
    <div class="bio">
      <p>Graham was awarded a Bachelor of Laws from the University of Western Australia in 1973. Since then Graham has been a partner at firms in Geraldton and Fremantle, as well as a principal of firms in Geraldton and Fremantle. In late 2009 Graham and his wife, Anne, made the decision to move back to Geraldton where they had previously lived for approximately 11 years. Graham has accumulated experience in a wide range of areas in over 45 years of legal practice, particularly in relation to agribusiness disputes and litigation, which is of great benefit to his clients.</p>
    </div>
    <div class="photo photo-vine" role="img" aria-label="Rows of autumn vineyard with a dirt track under a blue sky"></div>
  </section>
</div>

<div class="row-bottom">
  <!-- About -->
  <section class="panel col-1 about">
    <div class="strip"></div>
    <header class="masthead">
      <span class="seal" aria-hidden="true"></span>
      <div class="brand"><span class="brand-mark"></span><span class="brand-name">FERNGATE LEGAL</span></div>
      <span class="award" aria-hidden="true"></span>
    </header>
    <h2 class="band">About Us</h2>
    <div class="body">
      <ul class="dots">
        <li>Independent commercial law firm with offices in Geraldton and Perth</li>
        <li>Senior lawyers offering a combined 65 years of legal experience</li>
        <li>Practical advice in a professional and timely manner</li>
        <li>Client relationships built on trust</li>
        <li>Unfettered access to senior lawyers</li>
        <li>Direct and ongoing partner level involvement for each client</li>
        <li>Utilise the best information technology available to maintain high levels of efficiency and confidentiality</li>
      </ul>
    </div>
    <h2 class="band">Agribusiness Legal Awards</h2>
    <div class="body">
      <ul class="dots">
        <li>Ranked as a "Leading Agribusiness Law Firm – Western Australia, 2019" (Top 4)</li>
        <li>Ranked as a "Leading Agribusiness Law Firm – Western Australia, 2018" (Top 4)</li>
        <li>Ranked as a "Leading Agribusiness Law Firm – Western Australia, 2017" (Top 4)</li>
      </ul>
    </div>
    <h2 class="band">Quality Practice Standard</h2>
    <div class="body">
      <p>We are part of a select group of law firms which has been awarded the Quality Practice Standard by the state Law Society. As a result, we are able to better serve our clients by:</p>
      <ul class="dots">
        <li>Adopting modern quality management principles;</li>
        <li>Focusing on clients' requirements and client care; and</li>
        <li>Striving for consistency of service for all clients by all at the firm.</li>
      </ul>
    </div>
    <div class="photo photo-canola" role="img" aria-label="Flowering yellow canola field stretching to green hills"></div>
  </section>

  <!-- Expertise -->
  <section class="panel col-2 expertise">
    <div class="strip"></div>
    <header class="masthead">
      <span class="seal" aria-hidden="true"></span>
      <div class="brand"><span class="brand-mark"></span><span class="brand-name">FERNGATE LEGAL</span></div>
      <span class="award" aria-hidden="true"></span>
    </header>
    <h2 class="band">Expertise</h2>
    <div class="body" style="padding:8px 30px">
      <p>Over several decades our senior lawyers have advised clients involved in wheat, canola, lupin, wool, beef, dairy, wool, lamb, poultry, piggery, viticulture, forestry and plantation businesses.</p>
      <p>Our senior lawyers have strong family connections with pastoralists which allows them to better appreciate the challenges faced in agribusiness.</p>
      <p>Our family connection with pastoralists and our strong technical expertise in agribusiness law places Ferngate Legal in a unique position to advise clients in the agribusiness industry.</p>
      <p>We can assist with the following agribusiness matters:</p>
      <ul class="dots">
        <li>Agribusiness property contracts, agreements and deeds;</li>
        <li>Sale and purchase of agribusiness and farm assets;</li>
        <li>Pastoral lease advice;</li>
        <li>Native Title advice concerning access and compensation agreements;</li>
        <li>Land access agreements with mining, energy and telecommunications companies;</li>
        <li>Partnership, trust, corporation and joint venture advice;</li>
        <li>Farm Leases, Share Farming Agreements and Livestock Management Agreements;</li>
        <li>Carbon trading advice;</li>
        <li>Mortgages and securities;</li>
        <li>Farm succession planning, including Wills, Enduring Powers of Attorney and Guardianship;</li>
        <li>Employment advice;</li>
        <li>Deceased estates and probate, including advice concerning family provision claims;</li>
        <li>Disputes.</li>
      </ul>
    </div>
    <div class="photo photo-cattle" role="img" aria-label="Stockman on horseback mustering cattle in dusty sunset light"></div>
  </section>

  <!-- Experience -->
  <section class="panel col-3 exp">
    <div class="strip"></div>
    <header class="masthead">
      <span class="seal" aria-hidden="true"></span>
      <div class="brand"><span class="brand-mark"></span><span class="brand-name">FERNGATE LEGAL</span></div>
      <span class="award" aria-hidden="true"></span>
    </header>
    <h2 class="band">Expertise</h2>
    <div class="body">
      <p>Our senior lawyers have accumulated a wealth of experience in agribusiness law.</p>
      <p>Most of our work is subject to confidentiality which prevents us from disclosing any confidential information. However, we are able to disclose that our experience in agribusiness includes:</p>
      <ul class="dots">
        <li>Advising clients with respect to the sale and acquisition of farmland, including due diligence enquiries, preparation and review of contracts for sale, registration of securities and settlement.</li>
        <li>Advising farmer in relation to the 180-megawatt Banksia Ridge Wind Farm to be constructed on farmland near Carrow Flats, with a project value of up to AUD500 million and which is recognised as one of the best renewable projects in Australia.</li>
        <li>Advising pastoral lease holders on the sale and purchase of pastoral leases.</li>
        <li>Advising client on the termination of a vendor terms agreement for the sale of a farm and the repossession and resale of the farm.</li>
        <li>Advising numerous clients on various agreements with mining companies, including Royalty Agreements, Exploration Agreements, Land Access Deeds, Leases, Transmission Line Works Agreements, Deeds of Settlement and Release, Easement Deeds and Lay-Down Area Agreements.</li>
        <li>Advising on Access and Compensation Agreements with native title claimants.</li>
        <li>Advising client in relation to restructure of farmland and the transfer of the farmland to family members, trusts and a SMSF to qualify for the duties exemption under the Duties Act.</li>
        <li>Advising client in relation to the settlement of a farming partnership and trust dispute.</li>
        <li>Advising various farming families / corporate groups in relation to the restructuring of farm assets and exempt family farm transactions under the Duties Act.</li>
        <li>Advising farmers in relation to estate disputes and claims, including claims in the Supreme Court under the Family Provision Act.</li>
      </ul>
    </div>
    <div class="photo photo-sunset" role="img" aria-label="Outback sunset with a windmill silhouetted against an orange sky"></div>
  </section>
</div>

</body>
</html>
```